Paranormal Romance Author needs unique, eye-catching book covers for an entire series of books!

Author Mara Quillon is in need of outstanding, mind-blowing, unique, and eye-catching book covers for a paranormal romance series, called Wandering Embers. Initially we will only be asking for a design for the first book stated at the current price. Book 1: Wandering Embers. Once a winner is picked, the rest of the series will be negotiated (up to five more books. Possibly more.) The titles will be as following. Wandering Embers, Silver Embers, Hollow Embers, etc. Check out the unofficial description below. And if you would like a better feel for the book, the first five chapters have been attached as a document for your reading pleasure. :)In the hot and unforgiving Arizona desert, seventeen-year old Tessa Lindqvist finds herself in the most impossible of situations. When her boyfriend of ten years breaks up with her, she takes off into a storm, crashes her car, and dies. But then again, does she really? She is awaken during a battle and has been bitten. By a vampire. That's when young Captain Cole Harwick finds her. Going against everything he's been taught and trained for, he saves her from being killed by his men. She is still human after all. And a beautiful young girl at that. How could he bring himself to kill her?Tessa and Cole's tale is one of trials and torture, love and loss, but most of all, accepting one's own death. Will Cole safely see Tessa through her transformation to being a vampire? Will Tessa accept the immortal life that has ben thrust upon her? And will the two be able to part when the time comes, going off in their rightful positions, as enemies?Along with the author's name: Mara Quillon, and the book title, a tag-line shall be on the cover as well.Book 1: Wandering Embers, will have the tag-line "Do you know what dying feels like?"Images have been attached of book covers or art that speak to the author in her same genre. If human models are used on the cover, the author would prefer them to be smaller and farther away. But models are not imperative. If people are used, no bare-chested men that normally adorn adult romance covers. This series is guided for a young adult audience and must be done tastefully and fantastically, keeping a gothic, romantic feel. Basically the author seeks award-winning best-selling covers that are different and eye-catching, keeping the series covers similar for branding purposes. Think "series" and create a cover that can have a running theme. Have fun with this and most importantly, think outside of the box!!!*Note about character description. If model is used for Tessa, she is a young female aged 17 and has long white-blonde hair. Her eyes are violet-purple. The author prefers not to have a model for the male character at this point. And doesn't particularly care if a model is used as long as the design is striking.
Updates

4 participation payments have been added at $20.00 each. Thank you designers for all of your hard work. I know all too well how much goes into every design. :D Added Thursday, February 19, 2015

Just so everyone knows where they stand I have rated most of the designs. If you have a four or five star you are in the running for the win and may be asked to make some minor changes. If you have three or less stars, please feel free to resubmit a different design. If I have not yet rated your design it is because I am undecided at this time. A few days before the contest end date I will be running a pole to get feedback from colleagues, which may help me to make a better decision. At that point I will let the designers know where they stand and if they wish to resubmit a last design or two they can do so at that time. But please, for ANY of you that wish to keep submitting, feel free. I love seeing different ideas. I am also considering adding a second place prize, because I know how much work goes into this process. I appreciate everyone's submissions and thank you greatly for your time. -Mara Added Monday, February 23, 2015

Target Market(s)

Young adult and adult readers. Female mostly, some male, ages 15-38. :D

Industry/Entity Type

Adult

Font styles to use
Serif
Decorative
Script

Requirements
Must have
• The tagline 'Do you know what dying feels like?' must be somewhere on the book.
• Other than that, there are no must-haves but some ideas are...*Think magical, mystical, dreamy, romantic. *A close-up of a tombstone with the title engraved on it? Fog? Smoke? Maybe a flower at the bottom? Ivy? Vines?*Or anything with withering branches, moons, birds.*This story is set in the desert, so maybe desert scenery? But beautifully morbid?*If a model is used, one in distress, arms wrapped around knees? Suffering? If model is used, must have enough different shots of her to fill out an entire book series of six or possibly more.* I actually designed the lark tamsworth covers for myself. (attached) I love the whole broken up pictures idea. But I just can't seem to get it right. LOL. :D

```html
<!DOCTYPE html>
<html lang="en">
<head>
<meta charset="utf-8">
<title>Wandering Embers — Mara Quillon</title>
<link rel="stylesheet" href="https://fonts.googleapis.com/css2?family=Anton&family=Marcellus&display=swap">
<style>
  :root {
    --stage: #2c2c2c;
    --ink-black: #000000;
    --paper-white: #ffffff;
    --night-blue: #1c1f6e;
    --deep-blue: #2b33a0;
    --mid-blue: #4656c8;
    --pale-blue: #9aa6ea;
    --frost: #c9d0f5;
    --ember-gold: #d19a32;
    --bright-gold: #e8b850;
    --dark-gold: #6e4a14;
  }
  html, body {
    margin: 0;
    padding: 0;
    width: 973px;
    height: 1200px;
    overflow: hidden;
    background: var(--stage);
  }
  .book-cover {
    position: absolute;
    left: 157px;
    top: 135px;
    width: 660px;
    height: 930px;
    background: var(--ink-black);
    overflow: hidden;
  }
  .cover-artwork {
    position: absolute;
    left: 0;
    top: 0;
    width: 322px;
    height: 100%;
    background:
      radial-gradient(ellipse 45px 240px at 265px 520px, rgba(232,184,80,0.75), transparent 75%),
      radial-gradient(ellipse 70px 150px at 250px 360px, rgba(209,154,50,0.45), transparent 75%),
      radial-gradient(ellipse 50px 120px at 300px 700px, rgba(209,154,50,0.4), transparent 75%),
      radial-gradient(ellipse 70px 110px at 60px 140px, var(--frost), transparent 70%),
      radial-gradient(ellipse 90px 130px at 190px 90px, var(--pale-blue), transparent 70%),
      radial-gradient(ellipse 60px 140px at 110px 470px, var(--pale-blue), transparent 72%),
      radial-gradient(ellipse 100px 120px at 60px 640px, var(--frost), transparent 70%),
      radial-gradient(ellipse 90px 110px at 200px 820px, var(--pale-blue), transparent 72%),
      radial-gradient(ellipse 80px 100px at 170px 290px, var(--night-blue), transparent 75%),
      radial-gradient(ellipse 80px 120px at 120px 760px, var(--night-blue), transparent 75%),
      linear-gradient(170deg, var(--mid-blue) 0%, var(--deep-blue) 35%, var(--mid-blue) 60%, var(--deep-blue) 100%);
  }
  .tagline {
    position: absolute;
    top: 30px;
    left: 0;
    width: 100%;
    margin: 0;
    text-align: center;
    font-family: "Marcellus", serif;
    font-size: 22px;
    color: var(--paper-white);
  }
  .book-title {
    position: absolute;
    top: 206px;
    left: 0;
    width: 660px;
    margin: 0;
    text-align: center;
    font-family: "Anton", sans-serif;
    font-weight: 400;
    font-size: 126px;
    line-height: 120px;
    letter-spacing: 2px;
    color: var(--paper-white);
  }
  .book-title span { display: block; }
  .series-emblem {
    position: absolute;
    left: 208px;
    top: 572px;
    width: 240px;
    height: 240px;
  }
  .author-name {
    position: absolute;
    bottom: 22px;
    left: 0;
    width: 100%;
    margin: 0;
    text-align: center;
    font-family: "Marcellus", serif;
    font-size: 42px;
    letter-spacing: 1px;
    color: var(--paper-white);
  }
</style>
</head>
<body>
  <main class="book-cover">
    <div class="cover-artwork" role="img" aria-label="Cracked blue textured desert ground with a golden leafless tree"></div>
    <p class="tagline">Do you know what dying feels like?</p>
    <h1 class="book-title"><span>Wandering</span><span>Embers</span></h1>
    <svg class="series-emblem" viewBox="0 0 240 240" role="img" aria-label="Gold circular thorned series emblem">
      <defs>
        <radialGradient id="emblem-gold" cx="0.4" cy="0.35" r="0.75">
          <stop offset="0" stop-color="var(--bright-gold)"/>
          <stop offset="0.55" stop-color="var(--ember-gold)"/>
          <stop offset="1" stop-color="var(--dark-gold)"/>
        </radialGradient>
      </defs>
      <circle cx="120" cy="120" r="112" fill="url(#emblem-gold)" stroke="var(--paper-white)" stroke-width="6"/>
    </svg>
    <p class="author-name">MARA QUILLON</p>
  </main>
</body>
</html>
```